Pop-up Banner

Would like a design for a pop-up 85 x 206cm banner for a trade show. (from lumo press)
We would like "our logo" (northmere solutions) - then the tagline - "Your Trusted Partner in Data-Driven Decisions"
*Supporting Bullets*
Unified data, analytics & AI
Trusted insights, faster outcomes
Real-time intelligence at scale
Enterprise-ready, secure solutions
Clarity from data complexity
trusted by...some company logos
Partners with : partner logo
Our Colours: #FFA300, #3D4176, #FDD16E, #F87C57, #A68118, #1C2F36

```html
<!DOCTYPE html>
<html lang="en">
<head>
<meta charset="utf-8">
<title>Northmere Solutions – Pop-up Banner</title>
<link rel="stylesheet" href="https://fonts.googleapis.com/css2?family=Noto+Sans:wght@400;500;700;800&display=swap">
<style>
  :root {
    --orange: #FFA300;
    --navy: #3D4176;
    --ink: #1C2F36;
    --faint: #ECEDF2;
    --stage: #EEEEEE;
    --paper: #FFFFFF;
  }
  * { margin: 0; padding: 0; box-sizing: border-box; }
  html, body { width: 1200px; height: 1200px; overflow: hidden; background: var(--stage); }
  body { position: relative; font-family: "Noto Sans", Arial, sans-serif; }

  .banner {
    position: absolute; left: 381px; top: 71px;
    width: 438px; height: 1060px;
    background: var(--paper); overflow: hidden;
  }
  .banner-shapes { position: absolute; inset: 0; }

  .brand { position: absolute; left: 54px; top: 72px; display: flex; align-items: center; gap: 28px; }
  .brand-dot { width: 76px; height: 76px; border-radius: 50%; background: var(--orange); }
  .brand-name {
    color: var(--orange); font-weight: 700; font-size: 27px; line-height: 31px;
    letter-spacing: 0.5px; text-transform: uppercase;
  }

  .tagline {
    position: absolute; left: 56px; top: 278px; width: 360px;
    color: var(--navy); font-weight: 800; font-size: 40px; line-height: 45px;
    text-transform: uppercase;
  }

  .benefits {
    position: absolute; left: 84px; top: 551px;
    list-style: none; color: var(--paper); font-size: 17.5px; line-height: 27px;
  }
  .benefits li::before { content: "• "; }

  .client, .partner {
    position: absolute; display: flex; align-items: center; gap: 6px;
    color: var(--navy); font-weight: 500; white-space: nowrap;
  }
  .client { font-size: 20px; }
  .client-mark { width: 18px; height: 18px; background: var(--orange); }
  .client-mark.round { border-radius: 50%; background: var(--navy); }

  .partners-label {
    position: absolute; left: 134px; top: 880px; width: 170px; height: 34px;
    background: var(--navy); color: var(--paper); border-radius: 17px 6px 17px 6px;
    font-size: 18px; display: flex; align-items: center; justify-content: center;
  }
  .partner { font-size: 17px; }
  .partner-mark { width: 14px; height: 14px; border-radius: 50%; background: var(--ink); }
</style>
</head>
<body>
  <main class="banner">
    <svg class="banner-shapes" width="438" height="1060" viewBox="0 0 438 1060" aria-hidden="true">
      <defs>
        <clipPath id="lower-band"><rect x="0" y="541" width="438" height="300"/></clipPath>
      </defs>
      <circle cx="219" cy="466" r="269" fill="var(--faint)"/>
      <circle cx="219" cy="466" r="269" fill="var(--navy)" clip-path="url(#lower-band)"/>
    </svg>

    <header class="brand">
      <span class="brand-dot"></span>
      <span class="brand-name">Northmere<br>Solutions</span>
    </header>

    <h1 class="tagline">Your Trusted Partner in Data-Driven Decisions</h1>

    <ul class="benefits">
      <li>Unified data, analytics &amp; AI</li>
      <li>Trusted insights, faster outcomes</li>
      <li>Real-time intelligence at scale</li>
      <li>Enterprise-ready, secure solutions</li>
      <li>Clarity from data complexity</li>
    </ul>

    <div class="client" style="left:44px; top:776px;"><span class="client-mark"></span>Fluxwing</div>
    <div class="client" style="left:175px; top:776px;"><span class="client-mark round"></span>Ardvale</div>
    <div class="client" style="left:295px; top:776px;"><span class="client-mark"></span>Kestrel</div>
    <div class="client" style="left:73px; top:822px;">Orvanta</div>
    <div class="client" style="left:241px; top:822px;"><span class="client-mark"></span>Harbourline</div>

    <div class="partners-label">Partners with:</div>

    <div class="partner" style="left:76px; top:949px;"><span class="partner-mark"></span>clearlens</div>
    <div class="partner" style="left:244px; top:949px;"><span class="partner-mark"></span>Tessera</div>
    <div class="partner" style="left:104px; top:991px;">Quorix</div>
    <div class="partner" style="left:244px; top:991px;">Meridane</div>
  </main>
</body>
</html>
```